Klassisches Visitenkarten-Design mit braunen Farbtönen gesucht
Zielgruppe
Meine Firma bietet Pferdezahnbehandlungen, Pferdefütterungsberatung sowie Trensen- und Gebissanpassungen an. Ausserdem habe ich eine mobile Pferdewaage. Meine Kunden sind Pferdebesitzer der gehobenen Klasse, die gerne Geld in die Hand nehmen um ihr Tier korrekt zu halten/versorgen.
Ich setze bisher auf ein klassisches Design in braun Tönen.
Aufgabenstellung
Mir ist eine klare, schnörkellose Botschaft wichtig.
Ich möchte mich gerne mit klassischem, aber auch sehr schönem Design von der Konkurrenz abheben.
Der Fokus soll auf der wissenschaftlichen Arbeitsweise mit dem Partner Pferd liegen.
Im Anhang sind Fotos von der alten Visitenkarten. Dort fehlt mir aber die klare Linie.
Normalerweise arbeite ich mit der Schriftart Eurostyle, bin aber auch für neue Vorschläge offen.

```html
<!DOCTYPE html>
<html lang="de">
<head>
<meta charset="utf-8">
<title>EQUIVIA – Visitenkarte</title>
<link href="https://fonts.googleapis.com/css2?family=Saira:wght@400;700&display=swap" rel="stylesheet">
<style>
  :root {
    --page-bg: #ededed;
    --card-bg: #ffffff;
    --text-grey: #727272;
    --brand-brown: #552d10;
    --shadow-light: #b4b5bb;
    --shadow-dark: #777b82;
  }
  html, body {
    margin: 0;
    padding: 0;
    width: 1200px;
    height: 1200px;
    overflow: hidden;
    background: var(--page-bg);
    font-family: "Saira", sans-serif;
  }
  .sheet { position: relative; width: 1200px; height: 1200px; }
  .card-shadow {
    position: absolute;
    width: 723px;
    height: 468px;
    background: linear-gradient(120deg, var(--shadow-light), var(--shadow-dark));
  }
  .card {
    position: absolute;
    width: 723px;
    height: 468px;
    background: var(--card-bg);
    color: var(--text-grey);
  }
  .card--front { left: 238px; top: 80px; }
  .shadow--front { left: 248px; top: 90px; }
  .card--back { left: 238px; top: 643px; }
  .shadow--back { left: 248px; top: 653px; }

  .contact { position: absolute; left: 53px; top: 45px; }
  .contact p { margin: 0; }
  .person-name { font-weight: 700; font-size: 28px; line-height: 1; letter-spacing: 0.2px; }
  .credentials { margin-top: 24px !important; font-weight: 700; font-size: 21px; line-height: 24px; }
  .address { margin-top: 25px !important; font-size: 22px; line-height: 24px; font-weight: 400; }
  .reach { margin-top: 23px !important; font-size: 22px; line-height: 24.5px; font-weight: 400; }

  .brand-band {
    position: absolute;
    left: 0; right: 0;
    top: 337px;
    height: 12px;
    background: var(--brand-brown);
  }
  .brand-mark {
    position: absolute;
    display: flex;
    align-items: center;
    gap: 10px;
    color: var(--brand-brown);
    font-weight: 700;
    line-height: 1;
  }
  .card--front .brand-mark { left: 455px; top: 150px; font-size: 38px; }
  .card--back .brand-mark {
    left: 0; right: 0; top: 190px;
    justify-content: center;
    font-size: 60px;
  }
  .brand-dot { border-radius: 50%; background: var(--brand-brown); flex: none; }
  .card--front .brand-dot { width: 18px; height: 18px; }
  .card--back .brand-dot { width: 28px; height: 28px; }

  .services {
    position: absolute;
    left: 0; right: 0;
    text-align: center;
    font-weight: 700;
    font-size: 19.5px;
    line-height: 1;
    white-space: nowrap;
  }
  .card--front .services { top: 405px; }
  .card--back .services { top: 403px; }
</style>
</head>
<body>
<main class="sheet">
  <div class="card-shadow shadow--front"></div>
  <section class="card card--front">
    <div class="contact">
      <p class="person-name">Marlene T. Vogt</p>
      <p class="credentials">Agrarwissenschaften (Dr. sc.)<br>EQUIVIA</p>
      <p class="address">Lindenweg 14<br>79790 Tannbrunn/Südschwarzwald</p>
      <p class="reach">Telefon: +49 (0) 151 - 4038217<br>E-Mail: kontakt@equivia-pferd.de<br>Internet: www.equivia.de</p>
    </div>
    <div class="brand-mark"><span class="brand-dot"></span>EQUIVIA</div>
    <div class="brand-band"></div>
    <p class="services">Pferdezahnbehandlung&nbsp; *&nbsp; Pferdefütterungsberatung&nbsp; *&nbsp; Pferdewaage</p>
  </section>

  <div class="card-shadow shadow--back"></div>
  <section class="card card--back">
    <div class="brand-mark"><span class="brand-dot"></span>EQUIVIA</div>
    <p class="services">Pferdezahnbehandlung&nbsp; *&nbsp; Pferdefütterungsberatung&nbsp; *&nbsp; Pferdewaage</p>
  </section>
</main>
</body>
</html>
```